Corporate Vision/Mission Designs for the Office Walls

What we are looking for:

We are looking for design proposals to frame our mission, vision and values on our office walls

The designs need to be elegant, clean lines, simple, easy to follow and of course, should follow our brand guidelines.

Here's the copy:

For Boardoom:
Vision: Marlow Prestwick ignites people with passion enabling joy and lifetime memories

Mission: We are transforming the way property is bought.

For Garage
Purpose: We connect people with their dreams, turn dreams into reality.

For Entrance
Core Values
Honour
Passion
Sharing
Surprise
Fun

Vision & Mission will go in the boardroom
Core Values : at the Entrance
Purpose: in the Garage meeting room

Attachments to this project include:

a) Photos of the walls where they will go, and the current designs on the walls

b) brand guidelines

Industry/Entity Type

Office

Font styles to use
Decorative

Requirements
Must have
• Follow the brandguidelines, and colors.
• Green / use minimally

```html
<!DOCTYPE html>
<html lang="en">
<head>
<meta charset="utf-8">
<title>Core Values</title>
<link rel="stylesheet" href="https://fonts.googleapis.com/css2?family=Cabin:ital,wght@1,400&display=swap">
<style>
  :root {
    --bg-centre: #ffffff;
    --bg-edge: #ececec;
    --accent: #12b3a6;
    --ink: #4e5157;
  }
  html, body {
    margin: 0;
    padding: 0;
    width: 1200px;
    height: 848px;
    overflow: hidden;
  }
  .wall-panel {
    position: relative;
    width: 1200px;
    height: 848px;
    background: radial-gradient(ellipse at 50% 50%, var(--bg-centre) 35%, var(--bg-edge) 100%);
    font-family: "Cabin", "Gill Sans", sans-serif;
    font-style: italic;
    font-weight: 400;
  }
  .values-block {
    position: absolute;
    left: 348px;
    top: 160px;
    width: 504px;
    text-align: center;
  }
  .values-title {
    margin: 0;
    color: var(--accent);
    font-size: 72px;
    line-height: 78px;
    letter-spacing: 1px;
    font-weight: 400;
  }
  .values-rule {
    display: block;
    margin: 24px 0 0;
    width: 504px;
    height: 2px;
    background: var(--accent);
    border: 0;
  }
  .values-list {
    list-style: none;
    margin: 12px 0 0;
    padding: 0;
    color: var(--ink);
    font-size: 62px;
    line-height: 75px;
  }
</style>
</head>
<body>
  <main class="wall-panel">
    <section class="values-block">
      <h1 class="values-title">CORE VALUES</h1>
      <hr class="values-rule">
      <ul class="values-list">
        <li>Honour</li>
        <li>Passion</li>
        <li>Sharing</li>
        <li>Surprise</li>
        <li>Fun</li>
      </ul>
    </section>
  </main>
</body>
</html>
```